VARLEX CONSULTING / PROJECT MANAGEMENT WEB DESIGN

Design Brief: Varlex Consulting Website

I own 'VARLEX' business name and therefore can keep the name and logo simple i.e. VARLEX only and incorporate consulting / Project Management within the design or text.

Purpose:

The purpose of this project is to create a website for Varlex.com.au, a project management consulting company. The website will promote the company's services, allowing potential clients to learn more about Varlex and its capabilities. The website should be professional, easy to navigate, and provide all necessary information for potential clients.

Target Audience:

Clients in the Oil & Gas, LNG, and Chemical industry
Businesses and organizations in need of project management and engineering consultancy services
Potential clients looking for information about the company and its services
Key Elements:
Clean and modern design that reflects the company's professional image and incorporates the company logo

Clear and easy-to-use navigation menu

“Homepage” that promotes the company's main services and includes the company's mission statement.

Services:

PROJECT MANAGEMENT
PROJECT ENGINEERING
QUALITY MANAGEMENT AND PROCESS DEVELOPMENT
BUSINESS CASE DEVELOPMENT
ENGINEERING & DESIGN MANAGEMENT
CONCEPT STUDIES AND PROJECT SUPPORT
CONSTRUCTION MANAGEMENT
CONTRACT MANAGEMENT / CLAIMS PROCUREMENT / SUPPLY CHAIN SUPPORT
COMMERCIAL LIABILITY & RISK MANAGEMENT

Mission Statement:

"Our mission at Varlex is to provide expert project management and engineering consultancy services that help our clients achieve their goals and exceed their expectations. We will accomplish this by offering a full range of services, providing experienced and highly-qualified professionals, building strong relationships with our clients, continuously improving our services, and maintaining a reputation for excellence."

"About" page that includes client-supplied text about the company
"Contact" page with an editable form, email, and phone number for potential clients to get in touch with the company

Design Style:

Professional and modern
Clean and simple layout
Use of the company's colors and branding (subject to change)
Use of high-quality images that reflect the industry and services

Functionality:
Responsive design that is optimized for all devices and screen sizes

Website will be coded and uploaded to a content management system (CMS) for easy updates and maintenance
Website will be optimized for search engines and include all necessary SEO elements
Website will be fully tested for compatibility with all modern web browsers and devices
Website will be secured with an SSL certificate to ensure the safety of user data (client hosting includes SSL certificate).

Target Market(s)

Clients in the Oil & Gas, LNG, and Chemical industry Businesses and organizations in need of project management and engineering consultancy services Potential clients looking for information about the company and its services

Industry/Entity Type

Oil & Gas, LNG, and Chemical industry Businesses and organizations

Coding

Coded - Design and coding required

Number of Pages Required

3 page

Font styles to use
Sans Serif

Colors
0054AA
0677BA
7BADD7
CADEEF
E8F1F8
EB3D1F
EC4F4E
F09395
F8D3D4
FCEDEE
6B429C
8869AF
B7A5CE
E3DAEB
F3F0F8

Requirements
Must have
• HOME ABOUT AND CONTACT PAGE
Nice to have
• Fresh look, open to ideas
Should not have
• Stock images and hand shakes and meeting rooms..

```html
<!DOCTYPE html>
<html lang="en">
<head>
<meta charset="UTF-8">
<title>Varlex Resources – Project Management & Engineering Consultancy</title>
<link href="https://fonts.googleapis.com/css2?family=Outfit:wght@300;400;500;600;700&family=Poppins:wght@300;400;500&display=swap" rel="stylesheet">
<style>
:root{
  --blue:#0054AA;
  --blue-mid:#0677BA;
  --blue-soft:#7BADD7;
  --blue-pale:#CADEEF;
  --blue-bg:#E8F1F8;
  --red:#EB3D1F;
  --navy:#143a61;
  --ink:#1b2330;
  --muted:#5d6775;
  --white:#fff;
}
*{margin:0;padding:0;box-sizing:border-box}
html,body{width:1200px;height:4228px;overflow:hidden}
body{position:relative;background:var(--white);font-family:'Poppins',sans-serif;color:var(--ink)}
.abs{position:absolute}
.head{font-family:'Outfit',sans-serif}
.btn{position:absolute;background:var(--red);color:#fff;border-radius:30px;font:500 11px 'Outfit',sans-serif;letter-spacing:.5px;display:flex;align-items:center;justify-content:center;text-transform:uppercase}

/* header */
.site-header{position:absolute;left:0;top:0;width:1200px;height:86px;background:#fff;border-top:3px solid var(--blue);z-index:5}
.brand{position:absolute;display:flex;align-items:center;gap:8px;font:600 14px 'Outfit',sans-serif;color:var(--blue-mid)}
.brand-dot{width:26px;height:26px;border-radius:50%;background:var(--blue-mid)}
.nav a{position:absolute;top:36px;font:400 12px 'Poppins',sans-serif;color:var(--ink);text-decoration:none}
.call-circle{position:absolute;left:892px;top:25px;width:34px;height:34px;border-radius:50%;background:var(--blue);display:flex;align-items:center;justify-content:center}
.call-text{position:absolute;left:934px;top:26px;font:400 11px 'Poppins',sans-serif;color:var(--blue-mid);line-height:14px}
.call-text b{display:block;color:var(--ink);font:600 13px 'Outfit',sans-serif}

/* hero */
.hero-photo{position:absolute;left:0;top:86px;width:1200px;height:562px;background:linear-gradient(180deg,#c9b6c8 0%,#e2c4b4 38%,#9a8b84 62%,#4c4a55 85%,#34343c 100%)}
.hero-card{position:absolute;left:118px;top:213px;width:440px;height:304px;background:rgba(255,255,255,.95);border-radius:100px 0 100px 0}
.hero-title{position:absolute;left:167px;top:287px;font:600 30px 'Outfit',sans-serif;color:var(--navy)}
.hero-title span{color:var(--blue-mid)}
.hero-sub{position:absolute;left:167px;top:328px;font:400 24px 'Outfit',sans-serif;color:var(--ink)}
.hero-text{position:absolute;left:168px;top:374px;width:360px;font:400 11px/22px 'Poppins',sans-serif;color:var(--muted)}

/* about */
.about-band{position:absolute;left:0;top:648px;width:1200px;height:742px;background:var(--blue)}
.about-lower{position:absolute;left:0;top:1390px;width:1200px;height:1217px;background:var(--blue-bg)}
.about-photo{position:absolute;left:0;top:744px;width:533px;height:742px;border-radius:0 0 160px 0;background:linear-gradient(160deg,#7d8c96 0%,#4f5c66 40%,#8a6a52 70%,#3f4a55 100%);border-right:12px solid var(--blue);z-index:2}
.about-photo-wrap{position:absolute;left:0;top:730px;width:545px;height:14px;background:#0a4791}
.eyebrow{font:300 20px 'Outfit',sans-serif}
.about-eyebrow{position:absolute;left:589px;top:764px;color:#fff}
.about-title{position:absolute;left:589px;top:792px;font:600 38px 'Outfit',sans-serif;color:#fff}
.about-text{position:absolute;left:590px;top:855px;width:505px;font:400 12.5px/24px 'Poppins',sans-serif;color:#e3ecf7}
.feature{position:absolute;left:590px;width:505px;color:#fff}
.feature-icon{position:absolute;left:0;top:2px;width:20px;height:20px;border-radius:50%;background:var(--red);box-shadow:0 0 0 4px rgba(255,255,255,.18);display:flex;align-items:center;justify-content:center}
.feature h3{margin-left:34px;font:500 18px 'Outfit',sans-serif;letter-spacing:.3px}
.feature p{margin-left:34px;margin-top:8px;font:400 12px/24px 'Poppins',sans-serif;color:#e3ecf7}
.feature-line{position:absolute;left:599px;top:1020px;width:1px;height:210px;border-left:1px dashed rgba(255,255,255,.4)}

/* services */
.section-eyebrow{position:absolute;left:0;width:1200px;text-align:center;font:300 20px 'Outfit',sans-serif;color:var(--ink)}
.section-title{position:absolute;left:0;width:1200px;text-align:center;font:600 40px 'Outfit',sans-serif;color:var(--navy)}
.section-title span{color:var(--blue)}
.divider{position:absolute;left:543px;width:114px;height:10px}
.service-card{position:absolute;width:283px;height:366px;background:#fff;border-radius:0 0 60px 0;overflow:hidden}
.service-img{height:264px}
.service-card h4{position:absolute;left:24px;top:292px;font:400 19px/25px 'Outfit',sans-serif;color:var(--ink)}
.plus{position:absolute;left:222px;top:300px;width:34px;height:34px;border-radius:50%;background:var(--blue);color:#fff;display:flex;align-items:center;justify-content:center;font:300 20px 'Outfit',sans-serif}

/* mission */
.mission-box{position:absolute;left:274px;top:2681px;width:826px;height:443px;background:var(--blue);border-radius:90px 0 70px 0}
.mission-photo{position:absolute;left:107px;top:2730px;width:520px;height:348px;border:6px solid #fff;box-shadow:0 10px 30px rgba(0,0,0,.18);background:linear-gradient(150deg,#9fb7c9 0%,#c9a070 45%,#d86a2a 60%,#5c5c5c 100%)}
.mission-eyebrow{position:absolute;left:673px;top:2769px;color:#fff}
.mission-title{position:absolute;left:673px;top:2800px;font:600 40px 'Outfit',sans-serif;color:#fff}
.mission-text{position:absolute;left:673px;top:2864px;width:400px;font:400 12px/24px 'Poppins',sans-serif;color:#e3ecf7}

/* contact */
.contact-eyebrow{position:absolute;left:136px;top:3263px}
.contact-title{position:absolute;left:136px;top:3292px;font:600 40px 'Outfit',sans-serif;color:var(--navy)}
.contact-title span{color:var(--blue-mid)}
.contact-text{position:absolute;left:136px;top:3354px;width:350px;font:400 12px/24px 'Poppins',sans-serif;color:var(--muted)}
.info{position:absolute;left:136px;display:flex;gap:16px;align-items:flex-start}
.info-label{font:600 11px 'Outfit',sans-serif;color:var(--ink);letter-spacing:.3px}
.info-value{font:400 12px 'Poppins',sans-serif;color:var(--muted);margin-top:5px}
.info-phone{font:600 22px 'Outfit',sans-serif;color:var(--blue);margin-top:2px}
.contact-skyline{position:absolute;left:0;top:3420px;width:1200px;height:330px;background:linear-gradient(180deg,rgba(232,241,248,0) 0%,#e7edf3 100%)}

.form-card{position:absolute;left:598px;top:3246px;width:443px;height:558px;background:#fff;border-top:3px solid var(--blue);border-radius:60px 0 60px 0;box-shadow:0 10px 40px rgba(20,58,97,.12);z-index:3}
.form-card h5{position:absolute;left:32px;top:36px;font:400 20px 'Outfit',sans-serif;color:var(--ink)}
.field{position:absolute;left:34px;width:374px;border-bottom:1px solid #d7dde5}
.field label{display:block;font:500 11px 'Poppins',sans-serif;color:var(--ink)}
.field span{display:block;margin-top:8px;font:400 12px 'Poppins',sans-serif;color:#9aa2ad;padding-bottom:12px}

/* footer */
.footer-bg{position:absolute;left:0;top:3710px;width:1200px;height:518px}
.footer-brand{position:absolute;left:136px;top:3893px;font:600 19px 'Outfit',sans-serif;color:#fff}
.footer-mark{position:absolute;left:196px;top:3826px;width:46px;height:46px;border-radius:50%;background:#fff}
.footer-text{position:absolute;left:136px;top:3932px;width:235px;font:400 11px/21px 'Poppins',sans-serif;color:#d3deea}
.footer-col{position:absolute;top:3893px}
.footer-col h6{font:600 17px 'Outfit',sans-serif;color:#fff;letter-spacing:.3px}
.footer-col ul{list-style:none;margin-top:12px}
.footer-col li{font:400 11px 'Poppins',sans-serif;color:#e3ecf7;height:31px}
.subscribe-note{font:400 11px 'Poppins',sans-serif;color:#e3ecf7;margin-top:12px}
.email-input{position:absolute;left:834px;top:3971px;width:226px;height:35px;border-radius:20px;background:#fff;font:400 10px 'Poppins',sans-serif;color:#7a8390;padding:11px 16px}
.send{position:absolute;right:4px;top:4px;width:27px;height:27px;border-radius:50%;background:var(--red);display:flex;align-items:center;justify-content:center}
.follow{position:absolute;left:834px;top:4033px;font:400 11px 'Poppins',sans-serif;color:#fff}
.social{position:absolute;top:4028px;width:25px;height:25px;border-radius:50%}
.footer-rule{position:absolute;left:100px;top:4166px;width:1000px;height:1px;background:rgba(255,255,255,.2)}
.copyright{position:absolute;top:4197px;font:400 11px 'Poppins',sans-serif;color:#fff}
</style>
</head>
<body>

<header class="site-header">
  <div class="brand" style="left:148px;top:28px"><span class="brand-dot"></span>VARLEX RESOURCES</div>
  <nav class="nav">
    <a style="left:575px">Home</a>
    <a style="left:657px">About Us</a>
    <a style="left:758px">Contact Us</a>
  </nav>
  <svg class="abs" style="left:853px;top:34px" width="15" height="15" viewBox="0 0 15 15"><circle cx="6" cy="6" r="4.5" fill="none" stroke="#1b2330" stroke-width="1.6"/><line x1="9.5" y1="9.5" x2="13.5" y2="13.5" stroke="#1b2330" stroke-width="1.6"/></svg>
  <div class="call-circle"><svg width="16" height="16" viewBox="0 0 24 24"><path d="M6.6 10.8a15 15 0 006.6 6.6l2.2-2.2c.3-.3.7-.4 1-.2 1.1.4 2.3.6 3.6.6.6 0 1 .4 1 1V20c0 .6-.4 1-1 1A17 17 0 013 4c0-.6.4-1 1-1h3.5c.6 0 1 .4 1 1 0 1.3.2 2.5.6 3.6.1.3 0 .7-.2 1z" fill="#fff"/></svg></div>
  <div class="call-text">Call Now<b>+61 400 555 018</b></div>
</header>

<section>
  <div class="hero-photo" role="img" aria-label="Industrial power plant with chimneys at sunset"></div>
  <svg class="abs" style="left:0;top:86px" width="1200" height="562" viewBox="0 0 1200 562"><path d="M1200 400 C1140 520 960 560 560 562 L1200 562 Z" fill="#0054AA"/></svg>
  <div class="hero-card"></div>
  <h1 class="hero-title">PROJECT <span>MANAGEMENT</span></h1>
  <div class="hero-sub">&amp; Engineering Consultancy</div>
  <p class="hero-text">Lorem ipsum dolor sit amet, consectetur adipiscing elit, sed do eiusmod tempor incididunt ut labore et dolore magna.</p>
  <div class="btn" style="left:169px;top:437px;width:131px;height:34px">Get Started</div>
</section>

<section>
  <div class="about-band"></div>
  <div class="about-lower"></div>
  <div class="about-photo-wrap"></div>
  <div class="about-photo" role="img" aria-label="Engineer in blue hard hat inspecting plant equipment"></div>
  <div class="eyebrow about-eyebrow">About Us</div>
  <h2 class="about-title">VARLEX RESOURCES</h2>
  <p class="about-text">Lorem ipsum dolor sit amet, consectetur adipiscing elit, sed do eiusmod tempor incididunt ut labore et dolore magna aliqua ut enim ad minim veniam, quis nostrud exercitation ullamco laboris nisi ut aliquip ex ea commodo consequat duis aute irure dolor in reprehenderit in voluptate velit esse cillum dolore eu fugiat.</p>
  <div class="feature-line"></div>
  <div class="feature" style="top:992px"><span class="feature-icon"><svg width="10" height="10" viewBox="0 0 10 10"><path d="M1.5 5.2l2.3 2.3 4.7-5" fill="none" stroke="#fff" stroke-width="1.6"/></svg></span><h3>LOREM IPSUM DOLOR SIT AMET</h3><p>Lorem ipsum dolor sit amet, consectetur adipiscing elit, sed do eiusmod tempor incididunt ut labore et dolore magna aliqua ut ad minim.</p></div>
  <div class="feature" style="top:1095px"><span class="feature-icon"><svg width="10" height="10" viewBox="0 0 10 10"><path d="M1.5 5.2l2.3 2.3 4.7-5" fill="none" stroke="#fff" stroke-width="1.6"/></svg></span><h3>SED UT PERSPICIATIS UNDE</h3><p>Lorem ipsum dolor sit amet, consectetur adipiscing elit, sed do eiusmod tempor incididunt ut labore et dolore magna aliqua ut ad minim.</p></div>
  <div class="feature" style="top:1199px"><span class="feature-icon"><svg width="10" height="10" viewBox="0 0 10 10"><path d="M1.5 5.2l2.3 2.3 4.7-5" fill="none" stroke="#fff" stroke-width="1.6"/></svg></span><h3>CONTRARY TO POPULAR BELIEF</h3><p>Lorem ipsum dolor sit amet, consectetur adipiscing elit, sed do eiusmod tempor incididunt ut labore et dolore magna aliqua ut ad minim veniam, quis nostrud exercitation ullamco laboris nisi ut aliquip.</p></div>
</section>

<section>
  <div class="section-eyebrow" style="top:1531px">Varlex Resources</div>
  <h2 class="section-title" style="top:1558px">OUR <span>SERVICES</span></h2>
  <svg class="divider" style="top:1620px" viewBox="0 0 114 10"><line x1="0" y1="5" x2="40" y2="5" stroke="#7BADD7"/><circle cx="57" cy="5" r="5" fill="#0677BA"/><line x1="74" y1="5" x2="114" y2="5" stroke="#7BADD7"/></svg>

  <article class="service-card" style="left:144px;top:1673px"><div class="service-img" role="img" aria-label="Site supervisor with radio and tablet" style="background:linear-gradient(160deg,#c8d2da,#8a6a50 60%,#e07a2a)"></div><h4>Project<br>Management</h4><span class="plus">+</span></article>
  <article class="service-card" style="left:460px;top:1673px"><div class="service-img" role="img" aria-label="Engineer drafting plans with calculator and hard hat" style="background:linear-gradient(160deg,#e8c64a,#d8d8d2 45%,#a9a9a6)"></div><h4>Project<br>Engineeting</h4><span class="plus">+</span></article>
  <article class="service-card" style="left:773px;top:1673px"><div class="service-img" role="img" aria-label="Two engineers in safety vests reviewing a tablet" style="background:linear-gradient(160deg,#8a9aa6,#c4d84a 45%,#e0742a 75%,#5a6068)"></div><h4>Quality Management<br>&amp; Development</h4><span class="plus">+</span></article>
  <article class="service-card" style="left:144px;top:2078px"><div class="service-img" role="img" aria-label="Business documents and charts on a desk with laptop" style="background:linear-gradient(160deg,#b8a89a,#e6e2dc 50%,#9b7a5c)"></div><h4>Business Case<br>Develoment</h4><span class="plus">+</span></article>
  <article class="service-card" style="left:460px;top:2078px"><div class="service-img" role="img" aria-label="Team in hard hats around design drawings seen from above" style="background:linear-gradient(160deg,#9aa0a4,#e8e6e0 45%,#e6b83a 65%,#7a8288)"></div><h4>Engineering &amp; Design<br>Management</h4><span class="plus">+</span></article>
  <article class="service-card" style="left:773px;top:2078px"><div class="service-img" role="img" aria-label="Construction manager in hard hat on site" style="background:linear-gradient(160deg,#c9b894,#cddc4a 40%,#8aa6c8 70%,#6a6a6a)"></div><h4>Construction<br>Management</h4><span class="plus">+</span></article>

  <div class="btn" style="left:515px;top:2497px;width:170px;height:36px">View All Services</div>
</section>

<section>
  <div class="mission-box"></div>
  <div class="mission-photo" role="img" aria-label="Oil field workers in hard hats with a laptop beside a pump jack"></div>
  <div class="eyebrow mission-eyebrow">Varlex Resources</div>
  <h2 class="mission-title">MISSION STATEMENT</h2>
  <p class="mission-text">"Our mission at Varlex is to provide expert project management and engineering consultancy services that help our clients achieve their goals and exceed their expectations. We will accomplish this by offering a full range of services, providing experienced.</p>
  <div class="btn" style="left:678px;top:2991px;width:125px;height:36px">Learn More</div>
</section>

<section>
  <div class="contact-skyline" role="img" aria-label="Faint industrial skyline"></div>
  <div class="eyebrow contact-eyebrow">Contact Us</div>
  <h2 class="contact-title">GET IN <span>TOUCH</span></h2>
  <p class="contact-text">Lorem ipsum dolor sit amet, consectetur adipiscing elit, sed eiusmod tempor incididunt ut labore.</p>

  <div class="info" style="top:3430px">
    <svg width="40" height="40" viewBox="0 0 40 40" fill="none" stroke="#0677BA" stroke-width="1.6"><rect x="10" y="4" width="18" height="33"/><path d="M5 37h30"/><path d="M14 10h3M21 10h3M14 16h3M21 16h3M14 22h3M21 22h3M17 37v-8h4v8"/></svg>
    <div style="margin-top:4px"><div class="info-label">HEAD OFFICE</div><div class="info-value">32 Consectetur adipiscing eliteiusmod.</div></div>
  </div>
  <div class="info" style="top:3500px">
    <svg width="40" height="40" viewBox="0 0 40 40" fill="none" stroke="#0677BA" stroke-width="1.6"><path d="M4 16l16-11 16 11v20H4z"/><path d="M4 16l16 12 16-12"/><circle cx="20" cy="16" r="4"/></svg>
    <div style="margin-top:4px"><div class="info-label">EMAIL ADDRESS</div><div class="info-value">info@varlexresources.com</div></div>
  </div>
  <div class="info" style="top:3570px">
    <svg width="40" height="40" viewBox="0 0 24 24" fill="none" stroke="#0677BA" stroke-width="1"><path d="M6.6 10.8a15 15 0 006.6 6.6l2.2-2.2c.3-.3.7-.4 1-.2 1.1.4 2.3.6 3.6.6.6 0 1 .4 1 1V20c0 .6-.4 1-1 1A17 17 0 013 4c0-.6.4-1 1-1h3.5c.6 0 1 .4 1 1 0 1.3.2 2.5.6 3.6.1.3 0 .7-.2 1z"/></svg>
    <div style="margin-top:4px"><div class="info-label">CALL US NOW</div><div class="info-phone">+61 400 555 018</div></div>
  </div>

  <form class="form-card">
    <h5>Send Us A Message</h5>
    <div class="field" style="top:97px"><label>Name</label><span>Daniel Reeves</span></div>
    <div class="field" style="top:189px"><label>Email</label><span>daniel.reeves@mailbox.com</span></div>
    <div class="field" style="top:281px"><label>Name</label><span>0400 555 019</span></div>
    <div class="field" style="top:373px;height:88px"><label>Message</label><span>Type Your Message</span></div>
    <div class="btn" style="left:269px;top:492px;width:138px;height:36px">Submit Now</div>
  </form>
</section>

<footer>
  <svg class="footer-bg" viewBox="0 0 1200 518" preserveAspectRatio="none"><defs><linearGradient id="footerShade" x1="0" y1="0" x2="0" y2="1"><stop offset="0" stop-color="#1b4670"/><stop offset="1" stop-color="#0f2f51"/></linearGradient></defs><path d="M0 110 C0 40 40 0 140 0 L1200 0 L1200 518 L0 518 Z" fill="url(#footerShade)"/></svg>
  <div class="footer-mark"></div>
  <div class="footer-brand">VARLEX RESOURCES</div>
  <p class="footer-text">Lorem ipsum dolor sit amet, consectetur adipiscing elit, sed do eiusmod tempor incididunt ut labore.</p>
  <div class="footer-col" style="left:435px"><h6>QUICK LINKS</h6><ul><li>Home</li><li>About Us</li><li>Services</li><li>Contact Us</li></ul></div>
  <div class="footer-col" style="left:607px"><h6>OUR SERVICES</h6><ul><li>Project Management</li><li>Project Engineering</li><li>Management &amp; Development</li><li>Business Case Develoment</li><li>Construction Management</li></ul></div>
  <div class="footer-col" style="left:834px"><h6>SUBSCRIBE NEWSLETTER</h6><div class="subscribe-note">Subscribe to news &amp; updates</div></div>
  <div class="email-input">Email Address<span class="send"><svg width="12" height="12" viewBox="0 0 12 12"><path d="M1 6l10-5-4 10-1.5-4z" fill="#fff"/></svg></span></div>
  <div class="follow">Follow Us:</div>
  <span class="social" style="left:902px;background:#3b6a9a"></span>
  <span class="social" style="left:935px;background:#2a8fe0"></span>
  <span class="social" style="left:970px;background:#3b6a9a"></span>
  <div class="footer-rule"></div>
  <div class="copyright" style="left:136px">Copyright © 2023 Varlex Resources. All Rights Reserved</div>
  <div class="copyright" style="left:845px">Privacy Policy &nbsp;&nbsp;&nbsp;|&nbsp;&nbsp;&nbsp; Terms &amp; Conditions</div>
</footer>

</body>
</html>
```